Pipelining Product Supply Company Needs New Stationery

We need new stationery (letter head, with compliments slips & business card) for our industry leading pipe lining supply company. basically we sell product to other plumbers to carry out pipe relining.

Im looking for something, fresh, professional, sleek and modern at the same time.

Ive attached a copy of the logo and also some guidelines to follow for colours and fonts etc.

Target Market(s)

Plumbers

Industry/Entity Type

Plumbing

Font styles to use
Sans Serif

Requirements
Must have
• The logo, space for ABN, Address, Phone Number, website and email.
Nice to have
• Stand out from the crowd. To look sleep and professional.
Should not have
• Any other colours apart from what is on the guidelines.

```html
<!DOCTYPE html>
<html lang="en">
<head>
<meta charset="utf-8">
<title>Kestrel Relining Supply – Stationery</title>
<link href="https://fonts.googleapis.com/css2?family=Open+Sans:wght@400;600&family=Great+Vibes&display=swap" rel="stylesheet">
<style>
:root{
  --canvas:#e6e6e6;
  --paper:#ffffff;
  --forest:#0d4a14;
  --lime:#8dc63f;
  --brand:#4c9a2a;
  --charcoal:#231f20;
  --ink:#3a3a3a;
  --grey:#8a8a8a;
  --card-text:#c9c9c9;
}
*{box-sizing:border-box;margin:0;padding:0}
html,body{width:1200px;height:1200px;overflow:hidden}
body{background:var(--canvas);font-family:"Open Sans",sans-serif;color:var(--ink);position:relative}

.letterhead{position:absolute;left:40px;top:210px;width:600px;height:780px;background:var(--paper);display:flex;flex-direction:column}
.letterhead__head{text-align:center;padding-top:34px}
.brand{display:inline-flex;align-items:center;gap:8px;color:var(--brand);font-weight:600;letter-spacing:.06em;text-transform:uppercase}
.brand__dot{width:12px;height:12px;border-radius:50%;background:var(--brand)}
.letterhead .brand{font-size:21px}
.abn{font-size:12px;color:var(--ink);margin-top:6px}
.letterhead__body{padding:54px 48px 0;font-size:10.5px;line-height:2;flex:1}
.letterhead__body p{text-align:justify;margin-bottom:14px}
.recipient{margin-bottom:18px}
.signoff{font-size:14px;margin-top:6px}
.signature{font-family:"Great Vibes",cursive;font-size:30px;line-height:1.1}

.footer-band{border-top:3px solid var(--lime);margin-top:4px}
.footer-band__bar{background:var(--forest);color:#fff;text-align:center;font-size:12px;letter-spacing:.03em;margin-top:4px;padding:9px 0}

.card{position:absolute;left:670px;width:490px;height:278px;background:var(--charcoal)}
.card--front{top:210px;display:flex;align-items:center;padding:0 30px}
.card--front .brand{font-size:13px;width:190px}
.card__divider{width:1px;height:120px;background:var(--brand);margin:0 14px}
.card__details{font-size:10px;color:var(--card-text);line-height:1.55}
.card__name{color:var(--forest);font-size:15px;line-height:1.2}
.card__role{color:var(--lime);margin-bottom:6px}
.card__row{display:flex;align-items:center;gap:6px}
.card__row svg{width:10px;height:10px;fill:var(--lime);flex:none}
.card--back{top:500px;display:flex;align-items:center;justify-content:center}
.card--back .brand{font-size:18px}

.slip{position:absolute;left:670px;top:792px;width:490px;height:198px;background:var(--paper);display:flex;flex-direction:column}
.slip__head{text-align:center;padding-top:22px;flex:1}
.slip .brand{font-size:15px}
.slip .abn{font-size:10px;margin-top:3px}
.slip__title{text-align:center;font-size:22px;letter-spacing:.14em;color:#555;margin-bottom:6px}
.slip .footer-band__bar{font-size:9.5px;padding:7px 0}
</style>
</head>
<body>

<section class="letterhead">
  <header class="letterhead__head">
    <div class="brand"><span class="brand__dot"></span>Kestrel Relining Supply</div>
    <div class="abn">ABN. xxx-xxxx-xxxx</div>
  </header>
  <div class="letterhead__body">
    <p class="recipient">To<br>The,&nbsp; Director</p>
    <p>Lorem ipsum dolor sit amet, consectetur adipiscing elit. Sed at ante. Mauris eleifend, quam a varius dictum, massa quam dapibus leo, eget vulputate orci purus ut lorem. In fringilla mi in ligula. Pellentesque aliquam quam vel dolor. Nunc adipiscing. Sed quamodio, tempus ac, aliquam molestie varius tellus. Vestibulum ut nulla aliquam risus rutrum interdum. Pellentesque lorem.</p>
    <p>Curabitur sit amet erat quis risus feugiat viverra. Pellentesque augue justo, sagittis et, lacinia venenatis non, arcu. Nunc nec libero. In cursus dictum risus. Etiam tristique nisl a nulla. Ut a orci. Curabitur dolor nunc, egestas at, accumsan at, malesuada nec, magna. Nulla facilisi. Nunc volutpat. Vestibulum ante ipsum primis in faucibus orci luctus et ultrices posuere cubilia Curae; Ut sit amet orci vel mauris blandit vehicula. Nullam quis enim. Integer dignissim viverra velit. Curabitur in odio.</p>
    <p class="signoff">Thanking you,</p>
    <p class="signature">John Doe</p>
  </div>
  <footer class="footer-band">
    <div class="footer-band__bar">123-456-7890 | www.kestrelrelining.com | john@kestrelrelining.com | Dummy city, Dummy country, land</div>
  </footer>
</section>

<section class="card card--front">
  <div class="brand"><span class="brand__dot"></span>Kestrel Relining Supply</div>
  <span class="card__divider"></span>
  <div class="card__details">
    <div class="card__name">JOHN DOE</div>
    <div class="card__role">Director</div>
    <div>Dummy city</div>
    <div>Dummy country, land</div>
    <div class="card__row"><svg viewBox="0 0 10 10"><path d="M1 3 Q5 0 9 3 L8 4.5 L6.5 3.8 L6.5 3 Q5 2.5 3.5 3 L3.5 3.8 L2 4.5Z M2.5 5 H7.5 L8.5 9 H1.5Z"/></svg>123-456-7890</div>
    <div class="card__row"><svg viewBox="0 0 10 10"><circle cx="5" cy="5" r="4.5"/></svg>www.kestrelrelining.com</div>
    <div class="card__row"><svg viewBox="0 0 10 10"><path d="M0 2 H10 V8 H0Z"/></svg>john@kestrelrelining.com</div>
  </div>
</section>

<section class="card card--back">
  <div class="brand"><span class="brand__dot"></span>Kestrel Relining Supply</div>
</section>

<section class="slip">
  <header class="slip__head">
    <div class="brand"><span class="brand__dot"></span>Kestrel Relining Supply</div>
    <div class="abn">ABN. xxx-xxxx-xxxx</div>
  </header>
  <div class="slip__title">WITH COMPLIMENTS</div>
  <footer class="footer-band">
    <div class="footer-band__bar">123-456-7890 | www.kestrelrelining.com | john@kestrelrelining.com | Dummy city, Dummy country, land</div>
  </footer>
</section>

</body>
</html>
```